Linkmesa and Glimtoria advertising

We need Linkmesa and Glimtoria ads. Simple ad with Alaska themed background.
This ad is to introduce our new ZENIRO Internet service.
--Speeds to 500 mpbs
-- Packages start at only $89.99 for speeds to 100mbps
-- Fiber Optic based connection, Not satellite
-- Extreme low latency, consistent speeds
--FREE equipment, FREE Installation, FREE wifi router, First month of service FREE

```html
<!DOCTYPE html>
<html lang="en">
<head>
<meta charset="utf-8">
<title>Northvale Satellite – ZENIRO Internet</title>
<link rel="stylesheet" href="https://fonts.googleapis.com/css2?family=Anton&family=Poppins:ital,wght@0,500;0,600;0,700;1,600&display=swap">
<style>
  :root {
    --page: #ffffff;
    --snow-top: #6d7786;
    --snow-mid: #8a8f99;
    --snow-low: #c9ccd3;
    --offer-red: #d5202f;
    --offer-red-dark: #c01827;
    --brand-blue: #1d4f9a;
    --panel-blue: rgba(22, 78, 160, 0.9);
    --white: #ffffff;
    --logo-ink: #25282c;
    --router: #eef0f2;
  }
  * { margin: 0; padding: 0; box-sizing: border-box; }
  html, body { width: 1200px; height: 1000px; overflow: hidden; background: var(--page); }
  .canvas { position: relative; width: 1200px; height: 1000px; font-family: "Poppins", sans-serif; }

  .backdrop {
    position: absolute; left: 110px; top: 10px; width: 980px; height: 980px;
    background:
      linear-gradient(180deg, rgba(0,0,0,0) 40%, rgba(90,74,66,0.35) 55%, rgba(0,0,0,0) 75%),
      linear-gradient(180deg, var(--snow-top) 0%, var(--snow-mid) 45%, var(--snow-low) 80%, #e2e4e8 100%);
  }

  .brand {
    position: absolute; left: 724px; top: 98px;
    font-weight: 500; font-size: 36px; line-height: 44px;
    color: var(--logo-ink); letter-spacing: -0.5px;
  }

  .price-card {
    position: absolute; left: 145px; top: 162px; width: 455px; height: 330px;
    border-radius: 40px;
    background: linear-gradient(160deg, var(--offer-red), var(--offer-red-dark));
    color: var(--white); text-align: center;
  }
  .price-speed { font-family: "Anton", sans-serif; font-size: 90px; line-height: 1; margin-top: 52px; letter-spacing: 6px; }
  .price-lead { font-style: italic; font-weight: 600; font-size: 44px; line-height: 1; margin-top: 4px; }
  .price-amount { font-family: "Anton", sans-serif; font-size: 90px; line-height: 1; margin-top: 12px; letter-spacing: 2px; }

  .free-badge {
    position: absolute; left: 624px; top: 265px; width: 145px; height: 70px;
    background: var(--brand-blue); border: 2px solid var(--white);
    color: var(--white); font-weight: 700; font-size: 40px;
    display: flex; align-items: center; justify-content: center;
  }
  .free-bracket { position: absolute; left: 768px; top: 200px; }
  .free-item {
    position: absolute; left: 851px; color: var(--white);
    font-weight: 700; font-size: 26px; line-height: 33px; letter-spacing: 0.3px;
  }

  .feature-panel {
    position: absolute; left: 530px; top: 500px; width: 525px; height: 330px;
    border-radius: 40px; background: var(--panel-blue); color: var(--white);
    padding: 64px 0 0 22px;
  }
  .feature { display: flex; gap: 14px; font-weight: 700; font-size: 25px; line-height: 31px; margin-bottom: 22px; }
  .feature svg { flex: none; margin-top: 9px; }

  .router {
    position: absolute; left: 200px; top: 455px; width: 300px; height: 405px;
    background: linear-gradient(180deg, rgba(238,240,242,0) 0%, rgba(238,240,242,0.55) 50%, var(--router) 72%, #d9dcdf 100%);
    border-radius: 0 0 60px 60px;
  }

  .product-name {
    position: absolute; right: 152px; top: 895px;
    color: var(--white); font-weight: 500; font-size: 58px; letter-spacing: 2px; line-height: 1;
  }
</style>
</head>
<body>
<main class="canvas">
  <div class="backdrop" role="img" aria-label="Snowy Alaskan village with wooden cabins, pine trees and a lamp post under a winter sky"></div>

  <p class="brand">Northvale Satellite</p>

  <section class="price-card">
    <p class="price-speed">100MBPS</p>
    <p class="price-lead">at only</p>
    <p class="price-amount">$89.99</p>
  </section>

  <div class="free-badge">FREE</div>
  <svg class="free-bracket" width="80" height="210" viewBox="0 0 80 210" aria-hidden="true">
    <g stroke="#ffffff" stroke-width="2" fill="none">
      <line x1="0" y1="100" x2="37" y2="100"/>
      <line x1="37" y1="8" x2="37" y2="198"/>
      <line x1="37" y1="8" x2="70" y2="8"/>
      <line x1="37" y1="70" x2="70" y2="70"/>
      <line x1="37" y1="135" x2="70" y2="135"/>
      <line x1="37" y1="198" x2="70" y2="198"/>
    </g>
  </svg>
  <p class="free-item" style="top:191px">EQUIPMENT</p>
  <p class="free-item" style="top:254px">INSTALLATION</p>
  <p class="free-item" style="top:319px">WIFI ROUTER</p>
  <p class="free-item" style="top:383px">FIRST MONTH<br>OF SERVICE</p>

  <section class="feature-panel">
    <div class="feature">
      <svg width="14" height="14" viewBox="0 0 14 14" aria-hidden="true"><path d="M1 1 L13 7 L1 13 L5 7 Z" fill="#fff"/></svg>
      <p>SPEEDS TO 500 MPBS</p>
    </div>
    <div class="feature">
      <svg width="14" height="14" viewBox="0 0 14 14" aria-hidden="true"><path d="M1 1 L13 7 L1 13 L5 7 Z" fill="#fff"/></svg>
      <p>FIBER OPTIC BASED CONNECTION,<br>NOT SATELLITE</p>
    </div>
    <div class="feature">
      <svg width="14" height="14" viewBox="0 0 14 14" aria-hidden="true"><path d="M1 1 L13 7 L1 13 L5 7 Z" fill="#fff"/></svg>
      <p>EXTREME LOW LATENCY,<br>CONSISTENT SPEEDS</p>
    </div>
  </section>

  <div class="router" role="img" aria-label="White wifi router with two antennas standing in the snow"></div>

  <p class="product-name">ZENIRO</p>
</main>
</body>
</html>
```